Book Cover for Christian Book titled, "Climbing Past the Silver Hills"

Size of book cover will be 6" x 9".
The book is about how a person can know beyond a shadow of a doubt that they will go to heaven when they die.
The Title is "Climbing Past the Silver Hills"
Subtitle is "Finding Lasting Peace Through Daily Quiet Prayer and Reflection."
The front of the book should have title, subtitle, and author. The back of the book and spine should have no text and be a solid color.
The uploaded pic is a possibility for a design; but I'm open to other designs.
Whatever images are used need to be very high quality to meet Marrowind Folio Services guidelines. Also, the finished product needs to be sized to match the MFS guide for a 6x9 book.

```html
<!DOCTYPE html>
<html lang="en">
<head>
<meta charset="utf-8">
<title>Climbing Past the Silver Hills — Front Cover</title>
<link rel="stylesheet" href="https://fonts.googleapis.com/css2?family=Bebas+Neue&family=Poppins:wght@300;400&display=swap">
<style>
  :root {
    --page-bg: #ffffff;
    --sky-night: #0f1d3b;
    --sky-blue: #2c4a78;
    --sky-haze: #9fb0c2;
    --cloud-light: #e4e6e6;
    --sunrise-cream: #f1e8c6;
    --sun-gold: #d6a63a;
    --meadow-green: #6d8a2c;
    --forest-dark: #26371a;
    --title-white: #ffffff;
    --subtitle-ink: #1f1f22;
    --author-white: #f4f4f0;
  }
  * { margin: 0; padding: 0; box-sizing: border-box; }
  html, body {
    width: 1200px;
    height: 827px;
    overflow: hidden;
    background: var(--page-bg);
  }
  .stage {
    width: 1200px;
    height: 827px;
    display: flex;
    align-items: center;
    justify-content: center;
  }
  .book-cover {
    position: relative;
    width: 520px;
    height: 780px;
    overflow: hidden;
    box-shadow: 0 6px 24px rgba(0, 0, 0, 0.18);
  }
  .cover-landscape {
    position: absolute;
    inset: 0;
    background: linear-gradient(
      to bottom,
      var(--sky-night) 0%,
      var(--sky-blue) 22%,
      var(--sky-haze) 40%,
      var(--cloud-light) 52%,
      var(--sunrise-cream) 62%,
      var(--sun-gold) 69%,
      var(--meadow-green) 80%,
      var(--forest-dark) 100%
    );
  }
  .cover-title {
    position: absolute;
    top: 48px;
    left: 0;
    right: 0;
    padding-left: 24px;
    text-align: center;
    font-family: "Bebas Neue", "Arial Narrow", sans-serif;
    color: var(--title-white);
    line-height: 0.86;
    text-shadow: 0 2px 6px rgba(0, 0, 0, 0.25);
  }
  .cover-title span { display: block; }
  .title-line-lead { font-size: 82px; }
  .title-line-main { font-size: 104px; }
  .title-line-last { font-size: 118px; }
  .cover-subtitle {
    position: absolute;
    top: 366px;
    left: 60px;
    right: 40px;
    text-align: center;
    font-family: "Poppins", sans-serif;
    font-weight: 300;
    font-size: 20px;
    line-height: 1.4;
    color: var(--subtitle-ink);
  }
  .cover-author {
    position: absolute;
    bottom: 30px;
    left: 0;
    right: 0;
    padding-left: 16px;
    text-align: center;
    font-family: "Poppins", sans-serif;
    font-weight: 400;
    font-size: 15px;
    letter-spacing: 0.95em;
    color: var(--author-white);
  }
</style>
</head>
<body>
  <main class="stage">
    <section class="book-cover">
      <div class="cover-landscape" role="img" aria-label="Photograph of a sunrise over green countryside with trees and a small wooden barn beneath a deep blue sky with scattered clouds"></div>
      <h1 class="cover-title">
        <span class="title-line-lead">Climbing Past</span>
        <span class="title-line-main">The Silver</span>
        <span class="title-line-last">Hills</span>
      </h1>
      <p class="cover-subtitle">Finding Lasting Peace Through Daily Quiet Prayer and Reflection.</p>
      <p class="cover-author">AUTHOR NAME</p>
    </section>
  </main>
</body>
</html>
```